Velmira sailing boat for love and romance seekers*

We will pay extra 200$ for the winning design! So, we have a sailing boat, Harlow 58 KT called Velmira, which we’d like to give for charter in Turkey and maybe other countries. Need a dedicated web page, with gallery, calendar, videos, customer reviews, possibility to pay down payment, legal disclosures and in 3 languages (English, Russian and Turkish). Also, there should be info on toys and crew. We can also agree on a monthly fee for maintenance and updates. It’s really important to show the details, so that potential customers can see clearly that the boat is in perfect shape. If needed, we can even make a 3D of the interior, or any other materials that you might need. People should also have the possibility to see the sailing routes that they can chose and experience while cruising. Additionally, we can organize diving tours, surfing lessons, and any other activities.

Target Market(s)

Family with kids. Those people that are looking for more luxury than what’s usually offered with other boats. This is a middle segment between usual boats and super luxury boats. Also, it’s for those people that want romance, love and are looking for Unforgetable experiences with their family.

Coding

Coded - Design and coding required

Number of Pages Required

3 page

Font styles to use
Sans Serif

Requirements
Must have
• Boat has lots of options, and we have a tender boat with which one can waterski, pull ringos and other toys. It’s big enough to carry all guests at the same time and comfortable to reach safely any remote beach location. We have brand new snorkeling and diving equipment, new paddle and surfing boards, new dartino, Gorvetto and life jackets for all age groups. Also, we should have a page on crew, who they are and whom additionally they can chose (for example cook or cleaning staff).
Nice to have
• We’d like to see a page with will make you dream, feel romantic and in love. To ensure the visitors that our boat is perfect for a dream holiday. Imagine being in a secluded white sand beach bay all alone with your loved ones, in a beautiful luxurious boat. Now stop dreaming and join us to make your dreams come true. Lastly, because of virus, we should also mention that we do proper cleaning of boat after every use (COVID free).

Vēlmirā is a Sanskrit word that means "wandering" or "world", with the connotation of cyclic, circuitous change. It is also the concept of rebirth and "cyclicality of all life, matter, existence", a fundamental belief of most Indian religions. In short, it is the cycle of death and rebirth.
Should not have
• It should not be only for one system, all devices should be able to see that page properly.

```html
<!DOCTYPE html>
<html lang="en">
<head>
<meta charset="utf-8">
<title>Velmira — Sailing Charter</title>
<link href="https://fonts.googleapis.com/css2?family=Raleway:wght@600;700;800&family=Open+Sans:ital,wght@0,400;0,600;1,400&display=swap" rel="stylesheet">
<style>
:root{
  --teal:#17b3aa;
  --blue:#3d7fd0;
  --blue-head:#5b8fd6;
  --ink:#1b1b1b;
  --muted:#666;
  --grey-band:#eef0f1;
  --cell:#eef3fb;
  --cell-line:#c8d5ea;
  --booked:#e23a3a;
  --white:#fff;
}
*{box-sizing:border-box;margin:0;padding:0}
html,body{width:1200px;height:4850px;overflow:hidden}
body{position:relative;background:var(--white);font-family:"Open Sans",sans-serif;color:var(--ink)}
.abs{position:absolute}
.heading{font-family:"Raleway",sans-serif;font-weight:800;text-transform:uppercase;text-align:center;width:1200px;left:0;font-size:45px;letter-spacing:.5px}

/* hero */
.hero{left:0;top:0;width:1200px;height:760px}
.hero-photo{position:absolute;inset:0;background:linear-gradient(180deg,#c58d73 0%,#a1736a 18%,#476481 45%,#2e4a66 70%,#27405a 100%)}
.hero-wave{position:absolute;left:0;bottom:0}
.topbar{top:28px;right:58px;display:flex;align-items:center;gap:14px;font-size:15px;color:var(--white)}
.topbar .call b{font-weight:600}
.btn-join-sm{background:var(--teal);color:var(--white);font-family:"Raleway",sans-serif;font-weight:700;font-size:15px;padding:10px 18px}
.btn-login{border:2px solid var(--white);color:var(--white);font-family:"Raleway",sans-serif;font-weight:700;font-size:15px;padding:8px 22px}
.brand{left:110px;top:58px;font-family:"Raleway",sans-serif;font-weight:800;font-size:33px;color:var(--white)}
.menu{top:90px;left:366px;display:flex;gap:27px;font-family:"Raleway",sans-serif;font-weight:600;font-size:15px;color:var(--white);text-transform:uppercase}
.menu .active{color:var(--teal)}
.hero-title{left:110px;top:200px;font-family:"Raleway",sans-serif;font-weight:800;font-size:84px;color:var(--white)}
.hero-sub{left:112px;top:308px;font-size:25px;line-height:36px;color:var(--white);width:480px}
.btn-book{left:113px;top:415px;width:222px;height:62px;background:var(--teal);color:var(--white);font-family:"Raleway",sans-serif;font-weight:700;font-size:20px;display:flex;align-items:center;justify-content:center}
.play{left:562px;top:425px}

/* welcome */
.welcome-title{top:760px}
.welcome-text{left:200px;width:800px;top:838px;text-align:center;font-size:14px;line-height:29px;color:var(--muted)}
.btn-story{left:518px;top:948px;width:162px;height:52px;border:2px solid var(--teal);color:var(--teal);font-family:"Raleway",sans-serif;font-weight:700;font-size:16px;display:flex;align-items:center;justify-content:center}
.yacht{left:104px;top:1030px;width:990px;height:250px;background:linear-gradient(180deg,#f4f5f7 0%,#e6e9ee 60%,#c9d0da 100%)}

/* activities */
.activities{left:0;top:1338px;width:1200px;height:455px;background:var(--grey-band)}
.activities-title{top:1385px}
.card{width:307px;height:262px;top:1464px;background:var(--white);box-shadow:0 1px 3px rgba(0,0,0,.12)}
.card .photo{position:absolute;left:6px;top:6px;width:295px;height:198px}
.card .label{position:absolute;left:0;right:0;top:222px;text-align:center;font-size:22px;font-weight:600}

/* calendar */
.calendar-title{top:1842px}
.cal{left:107px;top:1931px;width:986px;height:418px;box-shadow:0 1px 4px rgba(0,0,0,.2)}
.cal-photo{position:absolute;left:0;top:0;width:340px;height:418px;background:linear-gradient(180deg,#6a7d96 0%,#c58f5e 45%,#d99a3e 60%,#3b3630 100%)}
.cal-grid{position:absolute;left:340px;top:0;width:646px;height:418px;border-collapse:collapse;table-layout:fixed}
.cal-grid .month th{background:var(--blue-head);color:var(--white);height:42px;font-weight:600;font-size:19px}
.cal-grid .days th{height:43px;font-weight:600;font-size:15px;border:1px solid var(--cell-line);background:var(--white)}
.cal-grid td{height:55.5px;border:1px solid var(--cell-line);background:var(--cell);text-align:center;font-size:15px;color:#555;line-height:17px}
.cal-grid td small{display:block;font-size:11px;font-weight:600}
.cal-grid td.booked small{color:var(--booked)}
.cal-grid td.available small{color:#2a8a3a}
.cal-grid td.sel{background:var(--teal);color:var(--white)}
.cal-grid td.sel small{color:var(--white)}

/* reviews */
.reviews-bg{left:0;top:2300px;width:1200px}
.reviews-title{top:2576px;color:var(--white)}
.review{width:307px;height:259px;top:2703px;background:var(--white);box-shadow:0 1px 4px rgba(0,0,0,.15);text-align:center}
.review .quote{position:absolute;left:20px;right:20px;top:64px;font-style:italic;font-size:13px;line-height:25px;color:#555}
.review .name{position:absolute;left:0;right:0;top:176px;font-size:17px;font-weight:600}
.review .role{position:absolute;left:0;right:0;top:204px;font-style:italic;font-size:15px;color:var(--teal)}
.avatar{top:2647px}
.dots{left:577px;top:2991px}

/* routes */
.routes-title{top:3068px}
.map{left:170px;top:3137px;width:885px;height:499px;background:linear-gradient(180deg,#e4e5e7 0%,#d6d8db 100%)}

/* gallery */
.gallery-title{top:3660px}
.tile{top:3749px;height:277px}
.gal-arrow{top:3868px}

/* cta */
.cta{left:0;top:4041px;width:1200px;height:400px}
.cta-photo{position:absolute;inset:0;background:linear-gradient(180deg,#5b6a72 0%,#3d4a4f 50%,#6b6250 100%)}
.cta-title{top:4100px;color:var(--white);font-size:45px;line-height:64px}
.btn-cta{left:488px;top:4254px;width:222px;height:60px;background:var(--teal);color:var(--white);font-family:"Raleway",sans-serif;font-weight:700;font-size:20px;display:flex;align-items:center;justify-content:center}

/* footer */
.foot-col{top:4552px}
.foot-col h4{font-family:"Raleway",sans-serif;font-weight:700;font-size:17px;margin-bottom:22px}
.foot-col li{list-style:none;font-size:15px;color:#666;line-height:30px}
.contact-row{display:flex;align-items:center;gap:16px;font-size:15px;color:#555;margin-bottom:26px}
.rule{left:109px;top:4763px;width:982px;height:1px;background:#d6d6d6}
.copy{left:110px;top:4788px;font-size:14px;color:#555}
.social{top:4781px;width:34px;height:34px;border:2px solid var(--blue);border-radius:50%}
</style>
</head>
<body>

<!-- Hero -->
<section class="abs hero">
  <div class="hero-photo" role="img" aria-label="Couple embracing on a yacht deck at sunset over the sea"></div>
  <svg class="hero-wave" width="1200" height="120" viewBox="0 0 1200 120">
    <path d="M0 120 L0 40 C200 110 420 10 640 60 C860 110 1000 60 1200 70 L1200 120 Z" fill="var(--teal)"/>
    <path d="M0 120 L0 62 C220 118 430 30 650 78 C860 122 1010 80 1200 86 L1200 120 Z" fill="var(--blue)"/>
    <path d="M0 120 L0 92 C230 130 440 58 660 96 C870 132 1010 100 1200 104 L1200 120 Z" fill="var(--white)"/>
  </svg>
</section>
<div class="abs topbar">
  <span class="call">&#9742; CALL US ON <b>1 555 010 2468</b></span>
  <span class="btn-join-sm">JOIN NOW</span>
  <span class="btn-login">LOGIN</span>
  <span>ENG &#8964;</span>
</div>
<div class="abs brand">VELMIRA</div>
<nav class="abs menu">
  <span class="active">Home</span><span>About Us</span><span>Services</span><span>Calendar</span><span>Gallery</span><span>News</span><span>Contact Us</span>
</nav>
<h1 class="abs hero-title">VELMIRA</h1>
<p class="abs hero-sub">Duis aute irure dolor in reprehenderit in voluptate velit esse cillum.</p>
<a class="abs btn-book">BOOK NOW</a>
<svg class="abs play" width="76" height="76" viewBox="0 0 76 76">
  <circle cx="38" cy="38" r="38" fill="rgba(20,30,40,.55)"/>
  <path d="M30 24 L54 38 L30 52 Z" fill="var(--white)"/>
</svg>

<!-- Welcome -->
<h2 class="abs heading welcome-title">Welcome to Velmira</h2>
<p class="abs welcome-text">Nemo enim ipsam voluptatem quia voluptas sit aspernatur aut odit aut fugit, sed quia consequu ntur magni dolores. Sos qui ratione voluptatem sequi nesciunt. Neque porro quisquam est, qui dolorem ipsum quia dolor sit amet, consectetur, adipisci velit, sedq uia non numquam eius m.</p>
<a class="abs btn-story">OUR STORY</a>
<div class="abs yacht" role="img" aria-label="White luxury motor yacht in side view"></div>

<!-- Activities -->
<section class="abs activities"></section>
<h2 class="abs heading activities-title">Activities</h2>
<div class="abs card" style="left:111px"><div class="photo" role="img" aria-label="Waterskier towed behind a speedboat" style="background:linear-gradient(180deg,#2a4566,#3e6a8c 60%,#d9e2ea)"></div><div class="label">Waterski</div></div>
<div class="abs card" style="left:446px"><div class="photo" role="img" aria-label="Guests riding a yellow inflatable ringo" style="background:linear-gradient(180deg,#4f7a50,#2e6f9a 45%,#e0c32a 70%,#2a6a94)"></div><div class="label">Pull Ringos</div></div>
<div class="abs card" style="left:782px"><div class="photo" role="img" aria-label="Divers entering turquoise water from a boat" style="background:linear-gradient(180deg,#1f9fae,#30b8c2 55%,#d7dfe3)"></div><div class="label">Diving Tours</div></div>
<svg class="abs" style="left:68px;top:1582px" width="18" height="30" viewBox="0 0 18 30"><path d="M15 3 L4 15 L15 27" stroke="#999" stroke-width="3" fill="none"/></svg>
<svg class="abs" style="left:1114px;top:1582px" width="18" height="30" viewBox="0 0 18 30"><path d="M3 3 L14 15 L3 27" stroke="#999" stroke-width="3" fill="none"/></svg>

<!-- Calendar -->
<h2 class="abs heading calendar-title">Calendar</h2>
<div class="abs cal">
  <div class="cal-photo" role="img" aria-label="Sailboat deck and rigging at sunset"></div>
  <table class="cal-grid">
    <tr class="month"><th>&#9664;</th><th colspan="5">AUG 2020</th><th>&#9654;</th></tr>
    <tr class="days"><th>SUN</th><th>MON</th><th>TUE</th><th>WED</th><th>THU</th><th>FRI</th><th>SAT</th></tr>
    <tr><td></td><td></td><td></td><td></td><td></td><td></td><td>1</td></tr>
    <tr><td>2</td><td>3</td><td>4</td><td>5</td><td>6</td><td>7</td><td>8</td></tr>
    <tr><td class="booked"><small>BOOKED</small>9</td><td>10</td><td class="available sel"><small>&#10004; AVAILABLE</small>11</td><td>12</td><td>13</td><td class="booked"><small>BOOKED</small>14</td><td>15</td></tr>
    <tr><td class="available"><small>&#10004; AVAILABLE</small>16</td><td>17</td><td>18</td><td class="booked"><small>BOOKED</small>19</td><td>20</td><td class="available"><small>&#10004; AVAILABLE</small>21</td><td>22</td></tr>
    <tr><td>23</td><td class="booked"><small>BOOKED</small>24</td><td>25</td><td class="available"><small>&#10004; AVAILABLE</small>26</td><td>27</td><td>28</td><td>29</td></tr>
    <tr><td>30</td><td>31</td><td></td><td></td><td></td><td></td><td></td></tr>
  </table>
</div>

<!-- Reviews -->
<svg class="abs reviews-bg" width="1200" height="720" viewBox="0 0 1200 720" role="img" aria-label="Aerial view of blue sea with boats">
  <defs><linearGradient id="sea" x1="0" y1="0" x2="0" y2="1"><stop offset="0" stop-color="#4a7fc8"/><stop offset=".55" stop-color="#6f9ad2"/><stop offset=".85" stop-color="#dfe9f6"/><stop offset="1" stop-color="#ffffff"/></linearGradient></defs>
  <path d="M0 170 C300 240 700 230 1000 110 C1100 70 1160 40 1200 25 L1200 720 L0 720 Z" fill="url(#sea)"/>
</svg>
<h2 class="abs heading reviews-title">Customer Reviews</h2>
<div class="abs review" style="left:98px"><p class="quote">“Nam libero tempore, cum soluta nobis est eligendi optio cumque nihil impedit quo minus id quod maxime placeat facere possi mus, omqumnis volup”</p><div class="name">Lucien Marbot</div><div class="role">Propriétaire - Marbot Studio</div></div>
<div class="abs review" style="left:446px"><p class="quote">“Nam libero tempore, cum soluta nobis est eligendi optio cumque nihil impedit quo minus id quod maxime placeat facere possi mus, omqumnis volup”</p><div class="name">Olivier Renaud</div><div class="role">Propriétaire - Azur Escapades</div></div>
<div class="abs review" style="left:795px"><p class="quote">“Nam libero tempore, cum soluta nobis est eligendi optio cumque nihil impedit quo minus id quod maxime placeat facere possi mus, omqumnis volup”</p><div class="name">Mathis Lorrain</div><div class="role">Propriétaire - Moment Doré</div></div>
<svg class="abs avatar" style="left:205px" width="94" height="94" viewBox="0 0 94 94"><circle cx="47" cy="47" r="47" fill="#c9d0d6"/><circle cx="47" cy="47" r="42" fill="#ffffff"/><circle cx="47" cy="36" r="14" fill="#c9d0d6"/><path d="M20 78 C24 58 70 58 74 78 Z" fill="#c9d0d6"/></svg>
<svg class="abs avatar" style="left:553px" width="94" height="94" viewBox="0 0 94 94"><circle cx="47" cy="47" r="47" fill="#c9d0d6"/><circle cx="47" cy="47" r="42" fill="#ffffff"/><circle cx="47" cy="36" r="14" fill="#c9d0d6"/><path d="M20 78 C24 58 70 58 74 78 Z" fill="#c9d0d6"/></svg>
<svg class="abs avatar" style="left:902px" width="94" height="94" viewBox="0 0 94 94"><circle cx="47" cy="47" r="47" fill="#c9d0d6"/><circle cx="47" cy="47" r="42" fill="#ffffff"/><circle cx="47" cy="36" r="14" fill="#c9d0d6"/><path d="M20 78 C24 58 70 58 74 78 Z" fill="#c9d0d6"/></svg>
<svg class="abs dots" width="46" height="14" viewBox="0 0 46 14"><circle cx="7" cy="7" r="6" fill="var(--teal)"/><circle cx="23" cy="7" r="5.5" fill="none" stroke="var(--teal)" stroke-width="1.5"/><circle cx="39" cy="7" r="5.5" fill="none" stroke="var(--teal)" stroke-width="1.5"/></svg>

<!-- Sailing routes -->
<h2 class="abs heading routes-title">Sailing Routes</h2>
<div class="abs map" role="img" aria-label="World map with highlighted routes and stops across the Mediterranean and Middle East"></div>

<!-- Gallery -->
<h2 class="abs heading gallery-title">Gallery</h2>
<div class="abs tile" style="left:0;width:288px;background:linear-gradient(180deg,#4b6b3e,#4a7d7d 55%,#2d8fb0)" role="img" aria-label="Sailboat anchored in a green bay"></div>
<div class="abs tile" style="left:303px;width:289px;background:linear-gradient(180deg,#3a7fa6,#b59a74 50%,#2f6f96)" role="img" aria-label="Guests relaxing on a floating platform"></div>
<div class="abs tile" style="left:607px;width:288px;background:linear-gradient(180deg,#8fa9bf,#3d78a8 40%,#e0652a 65%,#3b7aa6)" role="img" aria-label="People on orange kayaks"></div>
<div class="abs tile" style="left:910px;width:290px;background:linear-gradient(180deg,#a9c6e2,#3f6a3a 40%,#2f5a7a 60%,#d8c07a)" role="img" aria-label="Speedboat by a wooden jetty"></div>
<svg class="abs gal-arrow" style="left:10px" width="16" height="26" viewBox="0 0 16 26"><path d="M13 3 L4 13 L13 23" stroke="#fff" stroke-width="3" fill="none"/></svg>
<svg class="abs gal-arrow" style="left:1174px" width="16" height="26" viewBox="0 0 16 26"><path d="M3 3 L12 13 L3 23" stroke="#fff" stroke-width="3" fill="none"/></svg>

<!-- Call to action -->
<section class="abs cta">
  <div class="cta-photo" role="img" aria-label="Boat helm and seating overlooking the sea"></div>
  <svg style="position:absolute;left:0;bottom:0" width="1200" height="110" viewBox="0 0 1200 110">
    <path d="M0 110 L0 30 C260 90 520 10 760 40 C960 65 1080 50 1200 20 L1200 110 Z" fill="var(--teal)"/>
    <path d="M0 110 L0 50 C260 108 520 30 760 60 C960 84 1080 68 1200 40 L1200 110 Z" fill="var(--blue)"/>
    <path d="M0 110 L0 72 C260 120 520 50 760 80 C960 102 1080 88 1200 62 L1200 110 Z" fill="var(--white)"/>
  </svg>
</section>
<h2 class="abs heading cta-title">Stop dreaming &amp; join us<br>to make your dreams come true</h2>
<a class="abs btn-cta">JOIN NOW</a>

<!-- Footer -->
<div class="abs foot-col" style="left:109px"><h4>INFORMATION</h4><ul><li>About Us</li><li>Sailing</li><li>Gallery</li><li>Videos</li><li>News</li></ul></div>
<div class="abs foot-col" style="left:298px"><h4>SAILING</h4><ul><li>Search sailing opportunities</li><li>Advice for skippers and crew</li><li>Contributions</li><li>Directory</li></ul></div>
<div class="abs foot-col" style="left:556px"><h4>MEMBERSHIP</h4><ul><li>How it works</li><li>Membership plans</li><li>Sign up / register</li><li>Log in</li></ul></div>
<div class="abs foot-col" style="left:788px"><h4>CONTACT US</h4>
  <div class="contact-row"><svg width="34" height="34" viewBox="0 0 34 34"><circle cx="17" cy="17" r="16" fill="none" stroke="#c9d6ea" stroke-width="2"/><path d="M12 10 C11 15 15 22 22 24 L24 21 L20 19 L18 21 C16 20 14 18 13 16 L15 14 L13 10 Z" fill="var(--blue)"/></svg><span>1 555 010 2468</span></div>
  <div class="contact-row"><svg width="34" height="34" viewBox="0 0 34 34"><circle cx="17" cy="17" r="16" fill="#e6eef9"/><rect x="10" y="12" width="14" height="10" rx="1" fill="var(--blue)"/><path d="M10 12 L17 18 L24 12" stroke="#fff" stroke-width="1.5" fill="none"/></svg><span>info@velmira.com</span></div>
</div>
<div class="abs rule"></div>
<p class="abs copy">Copyright © 2020, Velmira All rights reserved.</p>
<span class="abs social" style="left:959px"></span>
<span class="abs social" style="left:1006px"></span>
<span class="abs social" style="left:1053px"></span>

</body>
</html>
```